Road Construction Company needs business cards

We would like a new business card designed for our business.

We're a road construction company based in Qld, Australia.

Can the business card please have the following information on it.

Name: Brent Halloway
Position: General Manager
Phone: 0491 257 314
Email: Brent.halloway@drovik.com.au
Address: 87 Margrove Ave, Tindale, QLD, 4016
Website: www.drovik.com.au

Visually we'd like the card to be professional and simple.

Attached is our logo.

Our website is www.drovik.com.au

Target Market(s)

Men aged 25-60

Contact Information for Business Card

As listed in project description

Font styles to use
Serif

Requirements
Must have
• Large logo on back of card

```html
<!DOCTYPE html>
<html lang="en">
<head>
<meta charset="utf-8">
<title>Drovik Business Cards</title>
<link href="https://fonts.googleapis.com/css2?family=Arimo:wght@400;700&display=swap" rel="stylesheet">
<style>
  :root {
    --bg: #e9e9ea;
    --card: #323232;
    --card-back: #2e2e2e;
    --brand-blue: #0a55a3;
    --accent-blue: #2f9fd8;
    --text-light: #f2f2f2;
    --logo-dark: #1f1f1f;
  }
  * { margin: 0; padding: 0; box-sizing: border-box; }
  html, body { width: 1200px; height: 802px; overflow: hidden; }
  body {
    background: var(--bg);
    font-family: "Arimo", Arial, sans-serif;
    display: flex;
    align-items: center;
    justify-content: center;
    gap: 60px;
  }
  .card {
    position: relative;
    width: 510px;
    height: 291px;
    overflow: hidden;
    box-shadow: 0 6px 18px rgba(0,0,0,0.18);
  }
  .card-front { background: var(--card); }
  .card-back {
    background: var(--card-back);
    display: flex;
    align-items: center;
    justify-content: center;
  }
  .front-band { position: absolute; inset: 0; }
  .front-content {
    position: absolute;
    left: 34px;
    top: 40px;
    color: var(--text-light);
  }
  .brand-name {
    font-weight: 700;
    font-size: 46px;
    letter-spacing: 2px;
    color: var(--brand-blue);
    line-height: 1;
    margin-bottom: 18px;
  }
  .person-name {
    font-size: 19px;
    color: var(--accent-blue);
    text-transform: uppercase;
    line-height: 1.1;
  }
  .person-role { font-size: 13px; margin-bottom: 14px; }
  .address { font-size: 12.5px; line-height: 1.3; margin-bottom: 12px; }
  .contact-list { list-style: none; font-size: 12.5px; line-height: 1.45; }
  .contact-list li { display: flex; align-items: center; gap: 8px; }
  .contact-icon { width: 11px; height: 11px; flex: none; }
  .back-logo {
    font-weight: 700;
    font-size: 78px;
    letter-spacing: 4px;
    color: var(--logo-dark);
  }
</style>
</head>
<body>
  <section class="card card-front" aria-label="Business card front">
    <svg class="front-band" viewBox="0 0 510 291" aria-hidden="true">
      <polygon points="300,0 420,0 510,200 510,291 400,291" fill="var(--brand-blue)"/>
    </svg>
    <div class="front-content">
      <div class="brand-name">DROVIK</div>
      <div class="person-name">Brent Halloway</div>
      <div class="person-role">General Manager</div>
      <div class="address">87 Margrove Ave<br>Tindale, QLD, 4016</div>
      <ul class="contact-list">
        <li>
          <svg class="contact-icon" viewBox="0 0 12 12"><path d="M2.5 1 L4.5 1 L5.3 3.4 L4 4.4 Q5 6.8 7.6 8 L8.6 6.7 L11 7.5 L11 9.5 Q11 11 9.5 11 Q1 10.5 1 2.5 Q1 1 2.5 1Z" fill="var(--accent-blue)"/></svg>
          0491 257 314
        </li>
        <li>
          <svg class="contact-icon" viewBox="0 0 12 12"><rect x="0.8" y="2.3" width="10.4" height="7.4" fill="none" stroke="var(--accent-blue)" stroke-width="1.2"/><path d="M1 2.6 L6 6.6 L11 2.6" fill="none" stroke="var(--accent-blue)" stroke-width="1.2"/></svg>
          Brent.halloway@drovik.com.au
        </li>
        <li>
          <svg class="contact-icon" viewBox="0 0 12 12"><circle cx="6" cy="6" r="5" fill="var(--accent-blue)"/><path d="M1 6 H11 M6 1 Q3 6 6 11 M6 1 Q9 6 6 11" fill="none" stroke="var(--card)" stroke-width="0.9"/></svg>
          www.drovik.com.au
        </li>
      </ul>
    </div>
  </section>

  <section class="card card-back" aria-label="Business card back">
    <div class="back-logo">DROVIK</div>
  </section>
</body>
</html>
```